Business Card Design Project

Company Name - Larkmere Med

Wellness consulting and training company. Run through a medical centre.

Main colour themes are orange and blue, as in the logo. Want to replicate same effect with business cards.

To give a sense of freedom and potential as per the company name.

Want the business card to be in line with stationary design, which I have launched as well.

Double sided with design and colour on one side and details on other side.
Updates

Reason: Need business card and stationary design to be teed up.

Target Market(s)

35 to 65 age group.
New age and trendy

Industry/Entity Type

Training

Requirements
Must have
• Colours orange and blue as per logo
Nice to have
• Design to be similar to stationary design, letterhead and envelopes

```html
<!DOCTYPE html>
<html lang="en">
<head>
<meta charset="utf-8">
<title>Larkmere Med – Business Card</title>
<link rel="stylesheet" href="https://fonts.googleapis.com/css2?family=Lato:wght@400;700;900&display=swap">
<style>
  :root {
    --blue: #1f5aa6;
    --blue-deep: #124486;
    --blue-light: #3f79bd;
    --orange: #e5701f;
    --ink: #1d1d1d;
    --paper: #ffffff;
    --paper-shade: #eeeeee;
    --backdrop: #e4e6e9;
  }
  * { box-sizing: border-box; margin: 0; padding: 0; }
  html, body {
    width: 1200px; height: 997px; overflow: hidden;
    background: var(--backdrop);
    font-family: "Lato", Arial, sans-serif;
  }
  .sheet {
    position: relative; width: 1200px; height: 997px;
  }
  .card {
    position: absolute; left: 220px;
    width: 760px; height: 434px;
    border-radius: 22px; overflow: hidden;
    background: linear-gradient(160deg, var(--paper) 0%, var(--paper) 55%, var(--paper-shade) 100%);
    box-shadow: 0 10px 30px rgba(0,0,0,.18);
  }
  .card--back { top: 50px; }
  .card--front { top: 514px; }

  /* back side */
  .back-band {
    position: absolute; left: 0; right: 0; top: 0; height: 58px;
    background: linear-gradient(90deg, var(--blue-light), var(--blue-deep));
  }
  .back-rule {
    position: absolute; left: 0; right: 0; top: 58px; height: 8px;
    background: var(--orange);
  }
  .back-brand {
    position: absolute; left: 0; right: 0; top: 180px;
    display: flex; align-items: center; justify-content: center; gap: 22px;
  }

  .brand-name {
    font-family: "Lato", Arial, sans-serif;
    font-weight: 400; color: var(--blue);
    white-space: nowrap; letter-spacing: -0.5px;
  }
  .brand-dot {
    border-radius: 50%; background: var(--orange); flex: none;
  }
  .back-brand .brand-name { font-size: 82px; }
  .back-brand .brand-dot { width: 34px; height: 34px; }

  /* front side */
  .front-brand {
    position: absolute; left: 48px; top: 170px;
    display: flex; align-items: center; gap: 12px;
  }
  .front-brand .brand-name { font-size: 44px; }
  .front-brand .brand-dot { width: 20px; height: 20px; }

  .divider {
    position: absolute; left: 372px; top: 42px; width: 4px; height: 250px;
    background: linear-gradient(180deg, rgba(31,90,166,.15), var(--blue) 45%, rgba(31,90,166,.05));
  }
  .holder {
    position: absolute; left: 408px; top: 50px;
  }
  .holder-name {
    font-weight: 900; font-size: 27px; color: var(--blue); letter-spacing: .3px;
  }
  .holder-role {
    font-weight: 700; font-size: 17px; color: var(--ink); margin-top: 1px;
  }
  .contacts {
    list-style: none; position: absolute; left: 408px; top: 138px;
  }
  .contacts li {
    display: flex; align-items: center; gap: 12px;
    font-size: 19px; font-weight: 700; color: var(--ink);
    height: 37px;
  }
  .contact-icon {
    width: 30px; height: 30px; border-radius: 50%;
    background: var(--orange); flex: none;
    display: flex; align-items: center; justify-content: center;
  }
  .contact-icon svg { width: 18px; height: 18px; }

  .front-rule {
    position: absolute; left: 0; right: 0; bottom: 96px; height: 8px;
    background: var(--orange);
  }
  .front-band {
    position: absolute; left: 0; right: 0; bottom: 0; height: 96px;
    background: linear-gradient(90deg, var(--blue-light), var(--blue) 50%, var(--blue-deep));
  }
</style>
</head>
<body>
<main class="sheet">

  <section class="card card--back" aria-label="Business card, reverse side">
    <div class="back-band"></div>
    <div class="back-rule"></div>
    <div class="back-brand">
      <span class="brand-name">Larkmere Med</span>
      <span class="brand-dot"></span>
    </div>
  </section>

  <section class="card card--front" aria-label="Business card, details side">
    <div class="front-brand">
      <span class="brand-name">Larkmere Med</span>
      <span class="brand-dot"></span>
    </div>

    <div class="divider"></div>

    <div class="holder">
      <p class="holder-name">YOUR NAME</p>
      <p class="holder-role">Centre Director</p>
    </div>

    <ul class="contacts">
      <li>
        <span class="contact-icon">
          <svg viewBox="0 0 24 24" fill="#fff"><path d="M3 8c0-2 4-4 9-4s9 2 9 4v2h-4V8.5c-1.3-.5-3-.8-5-.8s-3.7.3-5 .8V10H3z"/><path d="M6 11h12l2 8H4z"/><circle cx="12" cy="15" r="2" fill="#e5701f"/></svg>
        </span>
        +39 340 5512087
      </li>
      <li>
        <span class="contact-icon">
          <svg viewBox="0 0 24 24" fill="#fff"><path d="M6.6 10.8c1.4 2.8 3.8 5.1 6.6 6.6l2.2-2.2c.3-.3.7-.4 1-.2 1.1.4 2.3.6 3.6.6.6 0 1 .4 1 1V20c0 .6-.4 1-1 1C10.6 21 3 13.4 3 4c0-.6.4-1 1-1h3.5c.6 0 1 .4 1 1 0 1.3.2 2.5.6 3.6.1.3 0 .7-.2 1z"/></svg>
        </span>
        (+120) 555 0148
      </li>
      <li>
        <span class="contact-icon">
          <svg viewBox="0 0 24 24" fill="none" stroke="#fff" stroke-width="2"><rect x="3" y="6" width="18" height="12" rx="1" fill="#fff" stroke="none"/><path d="M3 6l9 7 9-7" stroke="#e5701f" stroke-width="1.6"/></svg>
        </span>
        info@larkmeremed.com
      </li>
      <li>
        <span class="contact-icon">
          <svg viewBox="0 0 24 24" fill="none" stroke="#fff" stroke-width="2.4" stroke-linecap="round"><path d="M10 14a4 4 0 0 0 5.7 0l3-3a4 4 0 0 0-5.7-5.7l-1 1"/><path d="M14 10a4 4 0 0 0-5.7 0l-3 3a4 4 0 0 0 5.7 5.7l1-1"/></svg>
        </span>
        www.larkmeremed.com
      </li>
    </ul>

    <div class="front-rule"></div>
    <div class="front-band"></div>
  </section>

</main>
</body>
</html>
```